Ulya Doner-Kebab Stationery Design Project

We are a factory of the Doner kebab to distribute for restaurants and supermarkets.

what I need is

1- Presentation Folders cover for (Brochure , Letter and Business Card), the size ( 9"x12" Closed)

2- Envelopes, Size (DL , C5 and C4)

3- Letterhead (Standard).

Target Market(s)

Restaurants and supermarkets

Industry/Entity Type

Business

Requirements
Must have
• -Try to make the design related to the Business.

-Choose the same colors of the logo (Yellow, red and white).

-Try to make it seriously and high class business.

- The main logo with white background

```html
<!DOCTYPE html>
<html lang="en">
<head>
<meta charset="utf-8">
<title>Ulya Doner-Kebab Stationery</title>
<link href="https://fonts.googleapis.com/css2?family=Questrial&display=swap" rel="stylesheet">
<style>
:root{
  --board:#353535;
  --paper:#f4f5f7;
  --red:#c0202c;
  --gold:#d4a535;
  --ink:#333333;
  --window:#cbcbcb;
  --mark:#e4e5e7;
  --rule:#c9c9c9;
}
*{box-sizing:border-box;margin:0;padding:0}
html,body{width:1200px;height:748px;overflow:hidden;background:var(--board)}
body{position:relative;font-family:"Questrial",Arial,sans-serif;color:var(--ink)}
.sheet{position:absolute;background:var(--paper);overflow:hidden}
.envelope{top:32px;height:178px}
.envelope--plain{left:175px;width:397px}
.envelope--swoosh{left:588px;width:398px}
.letterhead{top:254px;width:365px;height:472px}
.letterhead--footer{left:41px}
.letterhead--ruled{left:428px}
.letterhead--corner{left:811px}

.brand{position:absolute;display:flex;align-items:center;gap:5px}
.brand__dot{width:20px;height:20px;border-radius:50%;background:var(--gold);flex:none}
.brand__name{font-size:15px;color:var(--red);white-space:nowrap;line-height:1}
.envelope .brand{left:10px;top:44px}
.letterhead .brand{left:8px;top:20px}

.faint-mark{position:absolute;border-radius:50%;background:var(--mark)}

.small{font-size:6px;line-height:1.45;white-space:nowrap}
.contact{position:absolute;display:flex;align-items:center;gap:3px}
.icon{width:6px;height:6px;flex:none}

.window{position:absolute;left:188px;top:99px;width:150px;height:38px;border-radius:6px;background:var(--window)}
.envelope--swoosh .window{left:189px}

.gold-band{position:absolute;left:0;right:0;background:var(--gold)}
.red-tab{position:absolute;right:0;background:var(--red);border-top-left-radius:6px;color:#fff;font-size:12px;display:flex;align-items:center;justify-content:center}
.envelope .gold-band{bottom:0;height:11px}
.envelope--plain .red-tab{left:263px;bottom:0;height:19px}
.letterhead .gold-band{bottom:0;height:12px}
.letterhead .red-tab{left:211px;bottom:0;height:22px;font-size:11.5px}

.swoosh{position:absolute;inset:0}
.swoosh-url{position:absolute;right:12px;bottom:2px;color:#fff;font-size:12px}
.band-address{position:absolute;left:5px;bottom:3px;font-size:5px}

.divider{position:absolute;left:185px;top:30px;width:1px;height:46px;background:var(--red)}
.header-rule{position:absolute;left:14px;right:6px;top:86px;height:2px;background:var(--rule)}
</style>
</head>
<body>

<svg width="0" height="0" style="position:absolute">
  <defs>
    <symbol id="phone" viewBox="0 0 6 6"><rect x="1.2" y="0" width="3.6" height="6" rx="0.8" fill="#c0202c"/><rect x="1.8" y="0.8" width="2.4" height="3.2" fill="#f4f5f7"/></symbol>
    <symbol id="mail" viewBox="0 0 6 6"><rect x="0" y="1" width="6" height="4" fill="#c0202c"/><path d="M0 1 L3 3.4 L6 1" stroke="#f4f5f7" stroke-width="0.6" fill="none"/></symbol>
  </defs>
</svg>

<!-- DL envelope, plain -->
<section class="sheet envelope envelope--plain">
  <div class="faint-mark" role="img" aria-label="Faint brand emblem" style="left:275px;top:10px;width:120px;height:120px"></div>
  <div class="brand"><span class="brand__dot"></span><span class="brand__name">Ulya Doner-Kebab</span></div>
  <p class="small" style="position:absolute;left:11px;top:69px">PO Box 412, Mill Lane, Corvale, 40518</p>
  <div class="window"></div>
  <div class="contact small" style="left:7px;top:156px"><svg class="icon"><use href="#phone"/></svg>+1 55 0102031</div>
  <div class="contact small" style="left:68px;top:156px"><svg class="icon"><use href="#mail"/></svg>info@ulyadoner.com</div>
  <div class="gold-band"></div>
  <div class="red-tab">www.ulyadoner.com</div>
</section>

<!-- DL envelope, swoosh -->
<section class="sheet envelope envelope--swoosh">
  <div class="faint-mark" role="img" aria-label="Faint brand emblem" style="left:15px;top:20px;width:110px;height:110px"></div>
  <svg class="swoosh" viewBox="0 0 398 178" preserveAspectRatio="none">
    <path d="M398 178 V0 H362 C350 70 300 140 196 178 Z" fill="var(--red)"/>
    <path d="M0 168 H230 L210 178 H0 Z" fill="var(--gold)"/>
  </svg>
  <div class="brand"><span class="brand__dot"></span><span class="brand__name">Ulya Doner-Kebab</span></div>
  <div class="window"></div>
  <div class="contact small" style="left:7px;top:154px"><svg class="icon"><use href="#phone"/></svg>+1 55 0102031</div>
  <div class="contact small" style="left:68px;top:154px"><svg class="icon"><use href="#mail"/></svg>info@ulyadoner.com</div>
  <p class="band-address">PO Box 412, Mill Lane, Corvale, 40518</p>
  <p class="swoosh-url">www.ulyadoner.com</p>
</section>

<!-- Letterhead, footer contacts -->
<section class="sheet letterhead letterhead--footer">
  <div class="faint-mark" role="img" aria-label="Faint brand emblem" style="left:150px;top:150px;width:190px;height:190px"></div>
  <div class="brand"><span class="brand__dot"></span><span class="brand__name">Ulya Doner-Kebab</span></div>
  <div class="contact small" style="left:5px;top:440px"><svg class="icon"><use href="#phone"/></svg>+1 55 0102030</div>
  <div class="contact small" style="left:5px;top:450px"><svg class="icon"><use href="#mail"/></svg>info@ulyadoner.com</div>
  <p class="small" style="position:absolute;left:114px;top:440px">PO Box 412,<br>Mill Lane, Corvale, 40518</p>
  <div class="gold-band"></div>
  <div class="red-tab">www.ulyadoner.com</div>
</section>

<!-- Letterhead, ruled header -->
<section class="sheet letterhead letterhead--ruled">
  <div class="faint-mark" role="img" aria-label="Faint brand emblem" style="left:150px;top:150px;width:190px;height:190px"></div>
  <div class="brand" style="left:14px;top:40px"><span class="brand__dot"></span><span class="brand__name">Ulya Doner-Kebab</span></div>
  <div class="divider"></div>
  <p class="small" style="position:absolute;left:199px;top:30px">PO Box 412,<br>Mill Lane, Corvale, 40518</p>
  <div class="contact small" style="left:199px;top:51px"><svg class="icon"><use href="#phone"/></svg>+1 55 0102030</div>
  <div class="contact small" style="left:199px;top:60px"><svg class="icon"><use href="#mail"/></svg>info@ulyadoner.com</div>
  <div class="header-rule"></div>
  <div class="gold-band"></div>
  <div class="red-tab">www.ulyadoner.com</div>
</section>

<!-- Letterhead, corner contacts -->
<section class="sheet letterhead letterhead--corner">
  <div class="faint-mark" role="img" aria-label="Faint brand emblem" style="left:150px;top:150px;width:190px;height:190px"></div>
  <div class="brand" style="left:26px;top:40px"><span class="brand__dot"></span><span class="brand__name">Ulya Doner-Kebab</span></div>
  <p class="small" style="position:absolute;left:235px;top:30px">PO Box 412,<br>Mill Lane, Corvale, 40518</p>
  <div class="contact small" style="left:235px;top:51px"><svg class="icon"><use href="#phone"/></svg>+1 55 0102030</div>
  <div class="contact small" style="left:235px;top:60px"><svg class="icon"><use href="#mail"/></svg>info@ulyadoner.com</div>
  <div class="gold-band"></div>
  <div class="red-tab">www.ulyadoner.com</div>
</section>

</body>
</html>
```